Promotional Double-Sided postcard

We are promoting a web cam studio (www.velmorigrove.com) and making a postcard for recruiting models. I have attached a .doc of a very basic 8.5x11 flyer we drew up which contains the same information we want conveyed in the postcard. I've also attached our website's logo.

Industry/Entity Type

Promotional

```html
<!DOCTYPE html>
<html lang="en">
<head>
<meta charset="utf-8">
<title>Velmori Grove – Model Recruiting Postcard</title>
<link href="https://fonts.googleapis.com/css2?family=Arimo:ital,wght@0,400;0,700;1,700&family=Montserrat:ital,wght@1,900&display=swap" rel="stylesheet">
<style>
  :root {
    --magenta: #d4177e;
    --pink: #e0679f;
    --panel: #eef2f6;
    --ink: #2b2b2b;
    --grey: #5a5a5a;
    --green: #10994a;
    --white: #ffffff;
    --photo-warm: #d9b9a0;
    --photo-dark: #3a3a3a;
  }
  * { margin: 0; padding: 0; box-sizing: border-box; }
  html, body {
    width: 757px; height: 1200px; overflow: hidden; background: var(--white);
    font-family: "Arimo", Arial, sans-serif; color: var(--ink);
  }
  .card { position: absolute; left: 0; width: 757px; overflow: hidden; }
  .front { top: 0; height: 582px; background: var(--panel); border: 1px solid var(--magenta); }
  .back { top: 618px; height: 582px; border: 1px solid var(--magenta); background: var(--white); }

  .top-bar { position: absolute; top: 0; height: 24px; }
  .top-bar.main { left: 0; background: var(--magenta); }
  .top-bar.accent { background: var(--pink); }

  .brand { position: absolute; display: flex; align-items: center; gap: 8px;
    color: var(--magenta); font-weight: 700; font-size: 20px; white-space: nowrap; }
  .brand-dot { width: 30px; height: 30px; border-radius: 50%; background: var(--magenta); flex: none; }

  .headline { position: absolute; right: 30px; top: 52px; text-align: right; }
  .headline .amount { font-family: "Montserrat", Arial, sans-serif; font-style: italic; font-weight: 900;
    font-size: 62px; line-height: 1; color: var(--magenta); letter-spacing: -1px; }
  .headline .period { font-weight: 700; font-size: 35px; line-height: 1; color: var(--grey); margin-top: -2px; }

  .intro { position: absolute; z-index: 2; left: 28px; top: 164px; width: 700px; font-size: 15px; line-height: 21.5px;
    text-align: justify; color: var(--ink); }

  .photo { position: absolute; z-index: 1; }
  .photo.front-model { left: 0; top: 254px; width: 400px; height: 290px;
    background: linear-gradient(160deg, var(--photo-warm) 0%, #c69c82 35%, var(--photo-dark) 75%, #222 100%); }
  .photo.back-model { left: 0; top: 340px; width: 368px; height: 242px;
    background: linear-gradient(180deg, #f4f4f4 0%, var(--photo-warm) 45%, #8a5a40 100%); }

  .pitch { position: absolute; z-index: 2; right: 31px; top: 258px; text-align: right; color: var(--green);
    font-weight: 700; font-size: 14.5px; line-height: 17.5px; }
  .perks { position: absolute; z-index: 2; right: 31px; top: 335px; text-align: right; list-style: none;
    font-weight: 700; font-size: 11px; line-height: 17.2px; color: var(--ink); }

  .wave { position: absolute; z-index: 3; left: 0; bottom: 0; }
  .contact-front { position: absolute; z-index: 4; right: 32px; top: 506px; text-align: center; color: var(--white);
    font-weight: 700; font-size: 19px; line-height: 30px; }

  .left-panel { position: absolute; left: 0; top: 0; width: 368px; height: 582px; background: var(--panel); }
  .back-message { position: absolute; left: 0; width: 368px; top: 192px; text-align: center;
    font-weight: 700; font-size: 20.5px; line-height: 30px; color: var(--ink); }

  .mail-label { position: absolute; font-size: 20px; line-height: 27px; color: var(--ink); }
  .postage { left: 605px; top: 67px; text-align: center; }
  .address { left: 407px; top: 226px; }
  .barcode-label { left: 416px; top: 517px; }
  .address-line { position: absolute; left: 409px; width: 308px; height: 1px; background: var(--ink); }
</style>
</head>
<body>

<section class="card front">
  <div class="top-bar main" style="width:468px"></div>
  <div class="top-bar accent" style="left:468px;width:289px"></div>

  <div class="brand" style="left:30px;top:70px">
    <span class="brand-dot"></span>Velmori Grove
  </div>

  <div class="headline">
    <div class="amount">$3000</div>
    <div class="period">every month</div>
  </div>

  <p class="intro">That is a realistic number you can earn average working part-time as a live webcam model. Some full time models make that much in a WEEK, but think of what you could do with just an extra $3000 a month! If you’ve been given this flyer, it’s because YOU could be making great money as a live webcam model.</p>

  <div class="photo front-model" role="img" aria-label="Photo of a smiling woman in glasses leaning on a laptop with a webcam"></div>

  <p class="pitch">From the comfort of your home or in our<br>Beverly Hills cam studio,<br>we will help you discover one of the<br>most lucrative yet flexible jobs there is.</p>

  <ul class="perks">
    <li>* Free photo shoots for all models.</li>
    <li>* Artistic freedom.&nbsp; Nudity is entirely up to you.</li>
    <li>* Block anyone in Los Angeles<br>from ever seeing you online.</li>
    <li>* Friendly staff with studio access<br>available 24 hours a day, 7 days a week</li>
  </ul>

  <svg class="wave" width="757" height="140" viewBox="0 0 757 140" aria-hidden="true">
    <path d="M0 48 C130 88 270 110 430 70 C560 36 660 8 757 28 V140 H0 Z" fill="var(--pink)"/>
    <path d="M0 72 C140 110 280 118 430 92 C570 66 660 34 757 44 V140 H0 Z" fill="var(--magenta)"/>
  </svg>

  <div class="contact-front">www.velmorigrove.com<br>Call 18005550199</div>
</section>

<section class="card back">
  <div class="left-panel">
    <div class="top-bar main" style="width:228px"></div>
    <div class="top-bar accent" style="left:228px;width:140px"></div>

    <div class="brand" style="left:110px;top:108px">
      <span class="brand-dot"></span>Velmori Grove
    </div>

    <p class="back-message">Visit our website at<br>www.velmorigrove.com<br>to contact us with<br>any questions.<br>or Call 18005550199</p>

    <div class="photo back-model" role="img" aria-label="Photo of a woman with long wavy hair resting her chin on her hand"></div>

    <svg class="wave" width="368" height="90" viewBox="0 0 368 90" aria-hidden="true">
      <path d="M0 30 C90 62 170 70 250 36 C300 14 340 8 368 22 V90 H0 Z" fill="var(--pink)"/>
      <path d="M0 48 C90 78 180 82 260 54 C310 36 345 34 368 42 V90 H0 Z" fill="var(--magenta)"/>
    </svg>
  </div>

  <div class="mail-label postage">Postage<br>Area</div>
  <div class="mail-label address">AddressArea</div>
  <div class="address-line" style="top:294px"></div>
  <div class="address-line" style="top:325px"></div>
  <div class="address-line" style="top:357px"></div>
  <div class="address-line" style="top:389px"></div>
  <div class="mail-label barcode-label">Barcode Area</div>
</section>

</body>
</html>
```